quality electrical business needs a logo design

we need a logo design for our new company starting up. I'm a sole trader electrician. I want to make the PES prominent in Perant Electrical Services. Information I would want on the business card would be;
Business Name: Perant Electrical Services
What I do: Domestic/Commercial/Industrial Installation & Maintenance
Email Address: Bryce.perant@wavlo.net.au
Contact no: Bryce 0438261759
Electrical License no: EC57364

Open to different Colours but would like to see some with Navy blue. I want to promote professionalism and have a modern feel about it.

Industry/Entity Type

Electrical

```html
<!DOCTYPE html>
<html lang="en">
<head>
<meta charset="utf-8">
<title>Perant Electrical Services – Business Card</title>
<link href="https://fonts.googleapis.com/css2?family=Arimo:wght@400;700&display=swap" rel="stylesheet">
<style>
  :root {
    --backdrop: #2b2724;
    --signal-red: #e4291b;
    --signal-red-light: #f2432c;
    --navy-deep: #1d3241;
    --navy-slate: #4b6373;
    --ink-navy: #2f3d48;
    --paper-white: #ffffff;
    --muted-white: #d9e1e6;
  }
  * { box-sizing: border-box; margin: 0; padding: 0; }
  html, body {
    width: 1200px; height: 900px; overflow: hidden;
    background: var(--backdrop);
    font-family: "Arimo", Arial, sans-serif;
  }
  .canvas { position: relative; width: 1200px; height: 900px; }

  .card {
    position: absolute; width: 680px; height: 380px;
    box-shadow: 0 14px 34px rgba(0,0,0,0.45);
  }

  /* Front side */
  .card-front {
    left: 120px; top: 100px;
    background: linear-gradient(135deg, var(--signal-red) 0%, var(--signal-red-light) 100%);
    display: flex; align-items: center; justify-content: center; gap: 16px;
  }
  .front-dot {
    width: 46px; height: 46px; border-radius: 50%;
    background: var(--ink-navy);
  }
  .front-name {
    font-weight: 700; font-size: 52px; color: var(--ink-navy); letter-spacing: -1px;
  }

  /* Back side */
  .card-back {
    left: 440px; top: 470px;
    background: linear-gradient(90deg, var(--navy-deep) 0%, var(--navy-slate) 100%);
    color: var(--paper-white);
  }
  .brand {
    position: absolute; left: 52px; top: 148px;
    display: flex; align-items: center; gap: 12px;
  }
  .brand-dot {
    width: 58px; height: 58px; border-radius: 50%;
    background: var(--signal-red);
  }
  .brand-text { display: flex; flex-direction: column; }
  .brand-name {
    font-weight: 700; font-size: 50px; line-height: 44px; letter-spacing: -1px;
  }
  .brand-tagline {
    font-weight: 700; font-size: 13.5px; letter-spacing: 0.6px; margin-top: 4px;
  }
  .divider {
    position: absolute; left: 368px; top: 132px; width: 2px; height: 118px;
    background: var(--signal-red);
  }
  .contact { position: absolute; left: 390px; top: 130px; }
  .contact-name { font-weight: 700; font-size: 22px; margin-bottom: 14px; }
  .contact-line { font-size: 16px; line-height: 25px; }
  .licence { font-size: 9px; color: var(--muted-white); margin-top: 14px; }

  .services {
    position: absolute; left: 46px; top: 330px;
    font-weight: 700; font-size: 16px; display: flex; gap: 10px;
  }
  .services li { list-style: none; display: flex; align-items: center; gap: 6px; }
  .services li::before {
    content: ""; width: 7px; height: 7px; border-radius: 50%;
    background: var(--signal-red);
  }
</style>
</head>
<body>
<main class="canvas">
  <section class="card card-front" aria-label="Card front">
    <span class="front-dot"></span>
    <span class="front-name">Perant</span>
  </section>

  <section class="card card-back" aria-label="Card back">
    <div class="brand">
      <span class="brand-dot"></span>
      <div class="brand-text">
        <span class="brand-name">Perant</span>
        <span class="brand-tagline">ELECTRICAL SERVICES</span>
      </div>
    </div>
    <div class="divider"></div>
    <div class="contact">
      <p class="contact-name">Bryce Perant</p>
      <p class="contact-line">E: Bryce.perant@wavlo.net.au</p>
      <p class="contact-line">T: Bryce 0438261759</p>
      <p class="licence">Electrical License no: EC57364</p>
    </div>
    <ul class="services">
      <li>Domestic</li>
      <li>Commercial</li>
      <li>Industrial Installation &amp; Maintenance</li>
    </ul>
  </section>
</main>
</body>
</html>
```